Need Letterhead Design & Matching Business Card

I have a logo that I love already. But the letterhead is less than appealing and boring. I'd like a design for my letterhead which I will match with business cards. Also, I'd like to have used fonts that are generally available, as my current letterhead uses a font named "SPACE" which nobody has unless they download it...so when a Word version is forwarded, it looks awful on the receiver's screed due to not having the font. That being said, modern is the look we like and are going for.

My business is "Halloran Brightmoor PC" - a law firm specializing in representing people who have suffered catastrophic injuries or death (plane, auto, train crashes etc.).

See attached letterhead, which has all of the pertinent information. My logo is also attached in various formats.

```html
<!DOCTYPE html>
<html lang="en">
<head>
<meta charset="utf-8">
<title>Halloran Brightmoor PC — Stationery</title>
<link rel="stylesheet" href="https://fonts.googleapis.com/css2?family=Arimo:wght@400;700&family=Barlow+Semi+Condensed:wght@400;600&display=swap">
<style>
  :root{
    --slate:#39464f;
    --fold:#8c8c8c;
    --ink:#2b2b2b;
    --mark-alt:#2f2a29;
    --paper:#ffffff;
    --paper-shade:#eceef0;
    --backdrop:#f5f6f7;
    --edge:#dcdfe2;
  }
  *{margin:0;padding:0;box-sizing:border-box}
  html,body{width:1200px;height:1021px;overflow:hidden;background:var(--backdrop)}
  .canvas{position:relative;width:1200px;height:1021px;font-family:"Arimo",Arial,sans-serif;color:var(--ink)}

  .corner-art{position:absolute;background:linear-gradient(135deg,var(--slate) 0%,var(--slate) 55%,var(--fold) 100%)}

  /* Envelopes */
  .envelope{position:absolute;left:87px;width:490px;height:230px}
  .envelope--first{top:212px}
  .envelope--second{top:558px}
  .envelope__back{position:absolute;left:0;top:0;width:382px;height:202px;
    background:linear-gradient(#f4f5f7,#eef0f2)}
  .envelope__back svg{position:absolute;left:0;top:0;width:382px;height:66px}
  .envelope__front{position:absolute;left:107px;top:30px;width:382px;height:199px;
    background:linear-gradient(#ffffff 0%,#ffffff 60%,var(--paper-shade) 100%);overflow:hidden}
  .envelope__front .corner-art{right:0;top:0;width:150px;height:96px}
  .envelope__mark{position:absolute;left:51px;top:43px;width:42px;height:42px;background:var(--slate)}
  .envelope--second .envelope__mark{background:var(--mark-alt)}
  .envelope__name{position:absolute;left:31px;top:94px;font-weight:700;font-size:11px;line-height:14px;
    text-transform:uppercase;letter-spacing:.3px;color:var(--slate)}
  .envelope--second .envelope__name{color:var(--mark-alt)}
  .envelope__address{position:absolute;left:22px;top:131px;width:104px;text-align:center;
    font-size:7.2px;line-height:10.5px;color:#333}

  /* Letterhead */
  .letterhead{position:absolute;left:604px;top:122px;width:515px;height:777px;background:var(--paper);
    border:1px solid var(--edge);overflow:hidden}
  .letterhead .corner-art--top{left:0;top:0;width:170px;height:118px}
  .letterhead .corner-art--bottom{right:0;bottom:0;width:170px;height:54px;
    background:linear-gradient(315deg,var(--slate) 0%,var(--slate) 55%,var(--fold) 100%)}
  .letterhead__name{position:absolute;right:126px;top:50px;text-align:right;font-weight:700;
    font-size:17px;line-height:22px;text-transform:uppercase;letter-spacing:.4px;color:var(--ink)}
  .letterhead__mark{position:absolute;left:426px;top:38px;width:67px;height:67px;background:var(--mark-alt)}
  .letterhead__sender{position:absolute;left:28px;top:130px;color:var(--slate)}
  .letterhead__person{font-weight:700;font-size:12px;line-height:16px}
  .letterhead__address{font-size:11.5px;line-height:20px;color:#3a3a3a}
  .letterhead__contact{position:absolute;left:367px;top:118px;font-family:"Barlow Semi Condensed","Arial Narrow",sans-serif;
    font-size:11px;line-height:15.5px;color:#3a3a3a}
  .letterhead__web{font-weight:600;color:var(--ink)}
</style>
</head>
<body>
<main class="canvas">

  <section class="envelope envelope--first">
    <div class="envelope__back">
      <svg viewBox="0 0 659 114" preserveAspectRatio="none">
        <path d="M0 0H659Q659 30 652 60L185 60L185 112L95 112Q0 112 0 20Z" fill="var(--slate)"/>
      </svg>
    </div>
    <div class="envelope__front">
      <div class="corner-art" role="img" aria-label="Decorative folded-paper corner graphic"></div>
      <div class="envelope__mark"></div>
      <div class="envelope__name">Halloran<br>Brightmoor PC</div>
      <p class="envelope__address">4120 Larkspur Ave.<br>Suite 800<br>Fairmont Hills, CA 90318</p>
    </div>
  </section>

  <section class="envelope envelope--second">
    <div class="envelope__back">
      <svg viewBox="0 0 659 114" preserveAspectRatio="none">
        <path d="M0 0H659Q659 30 652 60L185 60L185 112L95 112Q0 112 0 20Z" fill="var(--slate)"/>
      </svg>
    </div>
    <div class="envelope__front">
      <div class="corner-art" role="img" aria-label="Decorative folded-paper corner graphic"></div>
      <div class="envelope__mark"></div>
      <div class="envelope__name">Halloran<br>Brightmoor PC</div>
      <p class="envelope__address">4120 Larkspur Ave.<br>Suite 800<br>Fairmont Hills, CA 90318</p>
    </div>
  </section>

  <section class="letterhead">
    <div class="corner-art corner-art--top" role="img" aria-label="Decorative folded-paper header graphic"></div>
    <div class="corner-art corner-art--bottom" role="img" aria-label="Decorative folded-paper footer graphic"></div>
    <div class="letterhead__name">Halloran<br>Brightmoor PC</div>
    <div class="letterhead__mark"></div>
    <div class="letterhead__sender">
      <p class="letterhead__person">R. Tomas Velden, Esq. | President</p>
      <p class="letterhead__address">4120 Larkspur Ave. | suite 800 &nbsp;I&nbsp;&nbsp; Fairmont Hills, CA 90318</p>
    </div>
    <div class="letterhead__contact">
      <p>tomas@halloranbrightmoor.com</p>
      <p>Tel: (555) 014-2290</p>
      <p class="letterhead__web">www.halloranbrightmoor.com</p>
    </div>
  </section>

</main>
</body>
</html>
```